Consulting company needs Business Cards - rough concept provided

I'm looking for someone to take our business card idea and make is slick and polished - to communicate our high-end, sophisticated, serious consulting business. We have a rough layout we did in-house. We are open to ideas on repo-ing elements, adjusting sizes, typefaces etc... within the general concept we've already come up with. We want it to be super-clean and sophisticated. We want to keep the white backgrounds, and blue brand colors. Our goal is to print with painted blue edges on thick cardstock. Thank you!!

```html
<!DOCTYPE html>
<html lang="en">
<head>
<meta charset="utf-8">
<title>Northvale Business Card</title>
<link rel="stylesheet" href="https://fonts.googleapis.com/css2?family=Poppins:wght@400;600;700;800&display=swap">
<style>
  :root {
    --backdrop: #e7e8ea;
    --card-white: #ffffff;
    --card-black: #06070a;
    --brand-blue: #29a3de;
    --ink: #111111;
    --muted: #a9a9a9;
  }
  * { margin: 0; padding: 0; box-sizing: border-box; }
  html, body {
    width: 1200px; height: 480px; overflow: hidden;
    background: var(--backdrop);
    font-family: "Poppins", sans-serif;
  }
  .canvas { position: relative; width: 1200px; height: 480px; }
  .card {
    position: absolute; top: 107.5px;
    width: 463px; height: 265px; overflow: hidden;
  }
  .card--front { left: 84.5px; background: var(--card-white); }
  .card--back { left: 653px; background: var(--card-black); }

  .wordmark { position: absolute; display: block; }
  .wordmark text {
    font-family: "Poppins", sans-serif; font-weight: 800;
    fill: var(--brand-blue);
  }
  .card--front .wordmark { left: 0; top: 0; width: 463px; height: 56px; }
  .card--back .wordmark { left: 68px; top: 112px; width: 327px; height: 42px; }

  .identity { position: absolute; left: 49px; top: 108px; }
  .identity__name { font-size: 13px; font-weight: 700; color: var(--ink); line-height: 1.2; letter-spacing: -0.1px; }
  .identity__first { color: var(--brand-blue); }
  .identity__role { font-size: 9.5px; font-weight: 400; color: var(--muted); margin-top: 2px; }
  .identity__rule { width: 26px; height: 1px; background: var(--brand-blue); margin-top: 5px; }

  .contact {
    position: absolute; left: 301px; top: 174px;
    border-left: 1px solid var(--brand-blue);
    padding-left: 13px; height: 41px;
    display: flex; flex-direction: column; justify-content: space-between;
  }
  .contact__row { display: flex; align-items: flex-start; gap: 8px; font-size: 7px; color: var(--ink); line-height: 1.2; }
  .contact__icon { width: 9px; height: 9px; flex: none; stroke: var(--brand-blue); fill: none; stroke-width: 1; }
</style>
</head>
<body>
<main class="canvas">
  <section class="card card--front" aria-label="Business card front">
    <svg class="wordmark" viewBox="0 0 463 56" aria-label="Northvale">
      <text x="0" y="55" font-size="78" textLength="463" lengthAdjust="spacingAndGlyphs">NORTHVALE</text>
    </svg>

    <div class="identity">
      <p class="identity__name"><span class="identity__first">Dana</span> Whitlock</p>
      <p class="identity__role">Brand Consultant</p>
      <div class="identity__rule"></div>
    </div>

    <div class="contact">
      <div class="contact__row">
        <svg class="contact__icon" viewBox="0 0 10 10"><path d="M5 9.5 C2.5 6.5 1.8 5 1.8 3.7 A3.2 3.2 0 0 1 8.2 3.7 C8.2 5 7.5 6.5 5 9.5Z"/><circle cx="5" cy="3.7" r="1.1"/></svg>
        <span>4820 Harbor Lane, Ste 210<br>Maple Grove, CA 90210</span>
      </div>
      <div class="contact__row">
        <svg class="contact__icon" viewBox="0 0 10 10"><path d="M2 1 L3.6 1 L4.3 3 L3.2 3.9 C3.8 5.2 4.8 6.2 6.1 6.8 L7 5.7 L9 6.4 L9 8 C9 8.6 8.5 9 8 9 C4.2 8.7 1.3 5.8 1 2 C1 1.5 1.4 1 2 1Z"/></svg>
        <span>(555) 014 2297</span>
      </div>
      <div class="contact__row">
        <svg class="contact__icon" viewBox="0 0 10 10"><circle cx="5" cy="5" r="4"/><ellipse cx="5" cy="5" rx="1.8" ry="4"/><path d="M1 5 H9 M1.6 3 H8.4 M1.6 7 H8.4"/></svg>
        <span>dana@northvale.com</span>
      </div>
    </div>
  </section>

  <section class="card card--back" aria-label="Business card back">
    <svg class="wordmark" viewBox="0 0 327 42" aria-label="Northvale">
      <text x="0" y="40" font-size="54" textLength="327" lengthAdjust="spacingAndGlyphs">NORTHVALE</text>
    </svg>
  </section>
</main>
</body>
</html>
```